Plakat-Design
Zielgruppe
Meine Firme trainiert Sportanfänger/Sportneueinsteiger in einem Gruppentraining oder Personaltraining. Im Unterricht, arbeiten wir nach meinem eigenen Konzept so dass jeder Kunde individuell nach seinen Leistungen eingestuft und gefördert werden können.
Aufgabenstellung
Das Schaufenster gliedert sich in fünf schmale Fenster (50x221cm) siehe Bild. Es soll auffallend, modern und professionell dargestellt werden.
Das Schaufenster soll zu verstehen geben, dass geführte Trainings im Gruppen- sowie im Personaltraining angeboten werden. beinhalten sollte es (Nicht ganz sicher ob dass zu viel text ist):
- Firmenname
- Firmenlogo
- Personaltraining & Gruppentraining
- Spezialisiert auf Sportanfänger und Sportneueinsteiger.
- Webseiten Name (eher klein)
- Bildliche Unterstreichung des Angebots.
www.lumavo-club.ch
Insta: lumavo.club.griesbach

```html
<!DOCTYPE html>
<html lang="de">
<head>
<meta charset="utf-8">
<title>Lumavo Club – Schaufenster Power Your Life</title>
<link rel="stylesheet" href="https://fonts.googleapis.com/css2?family=Montserrat:wght@600;700&display=swap">
<style>
  :root {
    --grey: #9e9893;
    --green-light: #2ea836;
    --green-mid: #24902f;
    --green-dark: #1c4f22;
    --green-text: #2a7a2c;
    --white: #ffffff;
    --frame: #3a3a3a;
    --mullion: #a39d94;
  }
  html, body { margin: 0; padding: 0; }
  body {
    width: 1200px; height: 2231px; overflow: hidden; position: relative;
    background: var(--white);
    font-family: "Montserrat", Arial, sans-serif;
  }
  .window-hero { position: absolute; left: 0; top: 0; width: 1200px; height: 700px; }
  .window-flat { position: absolute; left: 328px; top: 753px; width: 560px; height: 405px; }
  .window-svg text { font-family: "Montserrat", Arial, sans-serif; font-weight: 700; fill: var(--white); text-anchor: middle; }
  .window-flat .letter { font-size: 80px; }
  .window-flat .label { font-size: 12.5px; letter-spacing: 0.3px; }
  .window-flat .brand { font-size: 9px; fill: var(--green-dark); }
  .window-hero .letter { font-size: 124px; }
  .window-hero .label { font-size: 17px; letter-spacing: 0.3px; }
  .window-hero .brand { font-size: 13px; fill: var(--green-dark); }

  .photo-panel {
    position: absolute; width: 98px; top: 1260px; height: 407px;
    box-sizing: border-box; border: 1px solid var(--frame); overflow: hidden;
    background: var(--green-dark);
  }
  .photo-panel .panel-head {
    height: 66px; background: var(--white);
    display: flex; align-items: center; justify-content: center; gap: 4px;
  }
  .brand-name { font-weight: 700; font-size: 10px; color: var(--green-mid); letter-spacing: 0.2px; }
  .brand-dot { width: 7px; height: 7px; border-radius: 50%; background: var(--green-mid); }
  .photo-panel .panel-photo { position: absolute; left: 0; right: 0; top: 66px; bottom: 0; }
  .offer-list {
    position: absolute; left: 0; right: 0; top: 66px; bottom: 0;
    background: linear-gradient(160deg, var(--green-mid), var(--green-dark) 60%, #143a18);
    color: var(--white); font-weight: 700; font-size: 12.5px; line-height: 15px; text-align: center;
  }
  .offer-list span { position: absolute; left: 0; right: 0; }

  .print-col { position: absolute; top: 1808px; width: 100px; text-align: center; }
  .print-col .print-brand { display: flex; justify-content: center; align-items: center; gap: 4px; height: 30px; }
  .print-col .print-title {
    margin-top: 28px; height: 40px;
    font-weight: 700; font-size: 13.5px; line-height: 16px; color: var(--green-text);
  }
  .print-col .print-photo { position: absolute; top: 109px; left: 0; width: 100px; height: 281px; }
</style>
</head>
<body>

<svg class="window-svg window-hero" viewBox="0 0 1200 700" aria-label="Schaufenster Power Your Life in fünf Fensterflügeln">
  <defs>
    <clipPath id="hero-panes">
      <rect x="170" y="50" width="150" height="595"/>
      <rect x="340" y="50" width="150" height="595"/>
      <rect x="510" y="50" width="150" height="595"/>
      <rect x="680" y="50" width="150" height="595"/>
      <rect x="850" y="50" width="150" height="595"/>
    </clipPath>
  </defs>
  <rect x="150" y="30" width="870" height="635" fill="var(--mullion)"/>
  <g clip-path="url(#hero-panes)">
    <rect x="170" y="50" width="830" height="595" fill="var(--grey)"/>
    <g transform="translate(170,50) scale(1.482,1.469)">
      <polygon points="194,0 600,0 600,405 -58,405" fill="var(--green-light)"/>
      <polygon points="252,0 600,0 600,405 0,405" fill="var(--green-mid)"/>
      <polygon points="345,0 600,0 600,405 92,405" fill="var(--green-dark)"/>
      <polygon points="612,0 640,0 640,405 342,405" fill="var(--grey)"/>
    </g>
  </g>
  <g class="letter">
    <text x="245" y="197">P</text><text x="415" y="197">O</text><text x="585" y="197" textLength="126" lengthAdjust="spacingAndGlyphs">W</text><text x="755" y="197">E</text><text x="925" y="197">R</text>
    <text x="415" y="313">Y</text><text x="585" y="313">O</text><text x="755" y="313">U</text><text x="925" y="313">R</text>
    <text x="415" y="429">L</text><text x="585" y="429">I</text><text x="755" y="429">F</text><text x="925" y="429">E</text>
  </g>
  <g class="label">
    <text x="415" y="503">PERSONAL</text><text x="415" y="525">TRAINING</text>
    <text x="585" y="496">GRUPPEN</text><text x="585" y="518">TRAINING</text>
    <text x="755" y="492">ANFÄNGER</text>
    <text x="925" y="484">NEU</text><text x="925" y="506">EINSTEIGER</text>
  </g>
  <rect x="186" y="497" width="120" height="40" fill="var(--white)"/>
  <circle cx="198" cy="517" r="4" fill="var(--green-dark)"/>
  <text class="brand" x="252" y="522">LUMAVO.CLUB</text>
</svg>

<svg class="window-svg window-flat" viewBox="0 0 560 405" aria-label="Schaufenster Power Your Life, flache Ansicht">
  <defs>
    <clipPath id="pane-clip">
      <rect x="0" y="0" width="98" height="405"/>
      <rect x="118" y="0" width="98" height="405"/>
      <rect x="230" y="0" width="98" height="405"/>
      <rect x="345" y="0" width="98" height="405"/>
      <rect x="462" y="0" width="98" height="405"/>
    </clipPath>
  </defs>
  <g clip-path="url(#pane-clip)">
    <rect width="560" height="405" fill="var(--grey)"/>
    <polygon points="194,0 600,0 600,405 -58,405" fill="var(--green-light)"/>
    <polygon points="252,0 600,0 600,405 0,405" fill="var(--green-mid)"/>
    <polygon points="345,0 600,0 600,405 92,405" fill="var(--green-dark)"/>
    <polygon points="612,0 640,0 640,405 342,405" fill="var(--grey)"/>
  </g>
  <g class="letter">
    <text x="49" y="89">P</text><text x="167" y="89">O</text><text x="279" y="89" textLength="86" lengthAdjust="spacingAndGlyphs">W</text><text x="394" y="89">E</text><text x="511" y="89">R</text>
    <text x="167" y="170">Y</text><text x="279" y="170">O</text><text x="394" y="170">U</text><text x="511" y="170">R</text>
    <text x="167" y="251">L</text><text x="279" y="251">I</text><text x="394" y="251">F</text><text x="511" y="251">E</text>
  </g>
  <g class="label">
    <text x="167" y="311">PERSONAL</text><text x="167" y="327">TRAINING</text>
    <text x="279" y="311">GRUPPEN</text><text x="279" y="327">TRAINING</text>
    <text x="394" y="311">ANFÄNGER</text>
    <text x="511" y="311">NEU</text><text x="511" y="327">EINSTEIGER</text>
  </g>
  <rect x="4" y="299" width="90" height="30" fill="var(--white)"/>
  <circle cx="12" cy="314" r="3.5" fill="var(--green-dark)"/>
  <text class="brand" x="55" y="317">LUMAVO.CLUB</text>
</svg>

<div class="photo-panel" style="left:328px">
  <div class="panel-head"><span class="brand-dot"></span><span class="brand-name">LUMAVO.CLUB</span></div>
  <div class="panel-photo" role="img" aria-label="Foto: älterer Mann beim Langhanteltraining" style="background:linear-gradient(200deg,#9fb3c6,#5f6f86 55%,#3a4a3e)"></div>
</div>
<div class="photo-panel" style="left:446px">
  <div class="panel-head"><span class="brand-dot"></span><span class="brand-name">LUMAVO.CLUB</span></div>
  <div class="panel-photo" role="img" aria-label="Foto: Frau beim Training, grün getönt" style="background:linear-gradient(160deg,#5c8a5a,var(--green-mid) 45%,#1f5a25)"></div>
</div>
<div class="photo-panel" style="left:558px">
  <div class="panel-head"><span class="brand-dot"></span><span class="brand-name">LUMAVO.CLUB</span></div>
  <div class="offer-list">
    <span style="top:33px">PERSONAL<br>TRAINING</span>
    <span style="top:88px">GRUPPEN<br>TRAINING</span>
    <span style="top:153px">ANFÄNGER</span>
    <span style="top:195px">NEU<br>EINSTEIGER</span>
  </div>
</div>
<div class="photo-panel" style="left:673px">
  <div class="panel-head"><span class="brand-dot"></span><span class="brand-name">LUMAVO.CLUB</span></div>
  <div class="panel-photo" role="img" aria-label="Foto: Gruppentraining, dunkelgrün getönt" style="background:linear-gradient(170deg,#2d5a2e,#1c3f20 60%,#4a4640)"></div>
</div>
<div class="photo-panel" style="left:790px">
  <div class="panel-head"><span class="brand-dot"></span><span class="brand-name">LUMAVO.CLUB</span></div>
  <div class="panel-photo" role="img" aria-label="Foto: Training mit Kettlebell" style="background:linear-gradient(170deg,#24562a,#5b5048 55%,#3a3532)"></div>
</div>

<div class="print-col" style="left:322px">
  <div class="print-brand"><span class="brand-dot"></span><span class="brand-name">LUMAVO.CLUB</span></div>
  <div class="print-title">PERSONAL<br>TRAINING</div>
  <div class="print-photo" role="img" aria-label="Foto: Trainer betreut Kunden, grün getönt" style="background:linear-gradient(170deg,#2c8c33,#25462a 55%,#2a2f2a)"></div>
</div>
<div class="print-col" style="left:433px">
  <div class="print-brand"><span class="brand-dot"></span><span class="brand-name">LUMAVO.CLUB</span></div>
  <div class="print-title">GRUPPEN<br>TRAINING</div>
  <div class="print-photo" role="img" aria-label="Foto: Gruppe beim Training, grün getönt" style="background:linear-gradient(170deg,#3a5a38,#1f3a22 60%,#3e3a30)"></div>
</div>
<div class="print-col" style="left:550px">
  <div class="print-brand"><span class="brand-dot"></span><span class="brand-name">LUMAVO.CLUB</span></div>
  <div class="print-title">ANFÄNGER</div>
  <div class="print-photo" role="img" aria-label="Foto: Frau beim Training" style="background:linear-gradient(170deg,#4a5a48,#2a3a2a 55%,#26302a)"></div>
</div>
<div class="print-col" style="left:666px">
  <div class="print-brand"><span class="brand-dot"></span><span class="brand-name">LUMAVO.CLUB</span></div>
  <div class="print-title">WIEDER<br>EINSTEIGER</div>
  <div class="print-photo" role="img" aria-label="Foto: Training im Studio, grün getönt" style="background:linear-gradient(170deg,#4b3f3a,#2c8c33 45%,#3a3a36)"></div>
</div>
<div class="print-col" style="left:779px">
  <div class="print-brand"><span class="brand-dot"></span><span class="brand-name">LUMAVO.CLUB</span></div>
  <div class="print-title">NEU<br>EINSTEIGER</div>
  <div class="print-photo" role="img" aria-label="Foto: Trainer betreut Kunden, grün getönt" style="background:linear-gradient(170deg,#2c8c33,#25462a 55%,#2a2f2a)"></div>
</div>

</body>
</html>
```